Women's Shelter Website Design

We are working with a Women's Shelter in California. They provide services and shelter for women and mothers throughout California.
Some sites to use for inspiration:
https://harborlightcommons.org
https://qbrtl.org
https://www.kemjy.org
https://plmfarrowby.org
https://www.gvhollow.org (I love the banner, navigation and upper navigation)
https://bellmereroost.org (love the idea of an EXIT NOW button)
Thank you for taking the time to consider designing a website for us. We are web developers based in Stockton, CA, USA. Most of our projects go through the same process. Understanding this process may help you win a project with us. We custom-code all of our websites in-house. We don’t have any requirements as to what tools you use for your design, but we ask that you follow these guidelines.
IMAGES:
If you use any images or icons in the design, we ask that you have a link to the asset so we can purchase the image/icon. Most of the designs we submit do not have the customer’s images on them unless they have some great images. Be creative; show us the feeling you are trying to portray with your image choices. Use any royalty-free site you choose. We subscribe to Adobe and mainly use their images, but we can purchase images outside of Adobe. PLEASE NOTE: we will not submit designs to clients with watermarks on the images.
FONTS:
We ask that you identify the fonts you’re using in the design. This can be done in a message if you want. We typically use Google Fonts and Adobe Fonts.
CONTENT:
We're always open to different content and ideas. We often submit designs with stock images so the client can see our vision. We typically take pictures after the website launch to use their images with our vision. Lorem Ipsum is fine for paragraphs, but we ask that you make the Headers with correct English. We want to be able to show the vision and identify the sections of the website.
INSPIRATION:
We typically add a couple of links in the brief of websites we like to help you get started in your design.
REVISIONS:
We do not often ask for revisions of the designs unless we see something in the design that may not appeal to the client. If there are slight changes that we want to make, we do that in the development process.
FEEDBACK:
We rarely give feedback on designs during the design process. We are working on many website projects and do not have the time to provide feedback. We usually respond if your request is well thought out and asks specific questions, but a note asking “feedback, please” usually goes unanswered.

```html
<!DOCTYPE html>
<html lang="en">
<head>
<meta charset="utf-8">
<title>Lumina Women's Shelter</title>
<link rel="stylesheet" href="https://fonts.googleapis.com/css2?family=Ubuntu:wght@500;700&family=Open+Sans:wght@400;600&display=swap">
<style>
:root{
  --purple:#4a2183;--purple-deep:#3d1d78;--coral:#ff5e45;--green:#4caf50;
  --ink:#2b2b2b;--text:#555;--lavender:#ede6f6;--pink:#fddbd6;--beige:#efece6;--bar:#f4f4f4;
}
*{margin:0;padding:0;box-sizing:border-box}
html,body{width:1200px;height:3614px;overflow:hidden}
body{position:relative;background:#fff;font-family:"Open Sans",sans-serif;color:var(--text)}
.abs{position:absolute}
h2{position:absolute;font-family:"Ubuntu",sans-serif;font-weight:500;font-size:42px;color:var(--ink);line-height:1}
h2 .dot{display:inline-block;width:14px;height:14px;border-radius:50%;background:var(--purple);margin-right:12px;vertical-align:top}
p{font-size:15.5px;line-height:28px}
.btn{position:absolute;display:flex;align-items:center;justify-content:center;font-size:14px;text-transform:uppercase;background:var(--coral);color:#fff}
.btn.outline{background:#fff;color:var(--coral);border:2px solid var(--coral)}
.photo{position:absolute}
/* top bar */
.topbar{left:0;top:0;width:1200px;height:41px;background:var(--bar)}
.ribbon{position:absolute;top:0;height:41px;display:flex;align-items:center;justify-content:center;color:#fff;font-size:14px;font-weight:600;clip-path:polygon(0 0,100% 0,100% 0,100% 100%,0 100%,14px 50%)}
.nav{left:0;top:41px;width:1200px;height:67px;border-bottom:1px solid #e6e6e6}
.brand{position:absolute;left:111px;top:18px;display:flex;align-items:center;gap:8px;font-family:"Ubuntu",sans-serif;font-weight:700;font-size:28px;color:var(--ink)}
.brand i{width:14px;height:14px;border-radius:50%;background:var(--purple)}
.menu{position:absolute;left:363px;top:30px;display:flex;gap:29px;font-size:14px;color:var(--ink)}
/* hero */
.hero{left:0;top:108px;width:1200px;height:430px;overflow:hidden}
.hero .photo{left:0;top:0;width:760px;height:430px;background:linear-gradient(120deg,#8b6f5c,#c6b5a8 50%,#7d6a77)}
.crescent{position:absolute;left:618px;top:-150px;width:760px;height:730px;border-radius:50%;background:#e8e6e6}
.blob{position:absolute;left:634px;top:-130px;width:740px;height:700px;border-radius:50%;background:linear-gradient(45deg,#4b2588 25%,#a33b7c 60%,#ff6a4d 90%)}
.hero-text{position:absolute;left:728px;top:104px;color:#fff}
.hero-text .hi{font-size:24px}
.hero-text h1{font-family:"Ubuntu",sans-serif;font-weight:700;font-size:68px;line-height:1;margin-top:12px}
.hero-text .sub{font-size:23px;margin-top:14px}
.hero-btn{position:absolute;left:735px;top:274px;width:202px;height:40px;border:2px solid #fff;color:#fff;font-size:14px;display:flex;align-items:center;justify-content:center}
.exit{position:absolute;left:0;top:390px;width:138px;height:40px;background:var(--green);color:#fff;font-size:14px;display:flex;align-items:center;justify-content:center;gap:10px}
/* what we do */
.band-lav{left:0;top:1029px;width:1200px;height:463px;background:var(--lavender)}
.service{position:absolute;width:240px;text-align:center}
.service .ic{width:112px;height:112px;border-radius:50%;background:#fff;margin:0 auto;display:flex;align-items:center;justify-content:center;box-shadow:0 4px 12px rgba(74,33,131,.1)}
.service h3{font-family:"Ubuntu",sans-serif;font-weight:500;font-size:18px;color:var(--ink);margin-top:22px}
.service p{font-size:14.5px;line-height:27px;margin-top:12px}
.amt{position:absolute;top:1750px;height:48px;background:var(--purple);color:#fff;font-size:19px;display:flex;align-items:center;justify-content:center;box-shadow:0 4px 8px rgba(0,0,0,.2)}
/* impact */
.stat{position:absolute;width:163px;height:163px;border-radius:50%;background:#fff;display:flex;flex-direction:column;align-items:center;justify-content:center;text-align:center;box-shadow:inset 0 0 18px rgba(0,0,0,.12)}
.stat b{font-family:"Ubuntu",sans-serif;font-weight:500;font-size:42px;line-height:1.1}
.stat span{font-size:17px;color:var(--text);line-height:22px}
/* stories */
.band-beige{left:0;top:2443px;width:1200px;height:476px;background:var(--beige)}
/* connect */
.field{position:absolute;top:3173px;height:42px;border:1px solid #ddd;box-shadow:0 3px 8px rgba(0,0,0,.08);font-size:15px;color:#888;display:flex;align-items:center;padding-left:22px;background:#fff}
/* footer */
.footer{left:0;top:3304px;width:1200px;height:310px;background:linear-gradient(110deg,#d9504f 0%,#8d3c7a 45%,#4b2386 100%);color:#fff}
.footer .brand{left:111px;top:120px;color:#fff;font-size:36px}
.footer .brand i{background:#fff}
.social{position:absolute;left:164px;top:186px;display:flex;gap:6px}
.social i{width:23px;height:23px;border-radius:50%;background:#fff}
.fcol{position:absolute;top:56px;font-size:15px}
.fcol h4{font-weight:600;font-size:16px;margin-bottom:18px}
.fcol li{list-style:none;line-height:26px}
.fline{display:flex;gap:18px;align-items:flex-start}
.copy{position:absolute;left:0;width:1200px;top:277px;text-align:center;font-size:15px}
</style>
</head>
<body>

<div class="abs topbar">
  <div class="ribbon" style="left:683px;width:190px;background:#3eae5b">GET HELP NOW</div>
  <div class="ribbon" style="left:859px;width:154px;background:var(--coral)">VOLUNTEER</div>
  <div class="ribbon" style="left:999px;width:201px;background:var(--purple-deep)">DONATE</div>
</div>
<header class="abs nav">
  <div class="brand"><i></i>Lumina</div>
  <nav class="menu"><span>CAMPAIGN</span><span>ABOUT</span><span>WHAT WE DO</span><span>REAL STORIES</span><span>WAYS TO GIVE</span><span>GET INVOLVED</span><span>CONTACT</span></nav>
</header>

<section class="abs hero">
  <div class="photo" role="img" aria-label="Mother holding her young daughter with a teddy bear"></div>
  <div class="crescent"></div>
  <div class="blob"></div>
  <div class="hero-text">
    <div class="hi">Welcome to</div>
    <h1>Lumina</h1>
    <div class="sub">Women's Shelter in California</div>
  </div>
  <div class="hero-btn">GIVE HELP THAT WORKS</div>
  <div class="exit"><svg width="14" height="14" viewBox="0 0 14 14"><path d="M2 2l10 10M12 2L2 12" stroke="#fff" stroke-width="2"/></svg>EXIT NOW</div>
</section>

<h2 style="left:111px;top:614px"><span class="dot"></span>Our Mission</h2>
<div class="abs" style="left:111px;top:692px;width:480px">
  <p>Lorem ipsum dolor sit amet, consectetur adipisjdcing elit, sed do eiusmod tempor incididunt ut labore et dolornke magna aliqua. Quis ipsum suspendisse ultrices gravida. Risus commodo viverra maecenas accumsan lacus vel facilisis.</p>
  <p style="margin-top:8px">Lorem ipsum dolor sit amet, consectetur adipisjdcing elit, sed do eiusmod tempor incididunt ut labore et dolornke magna aliqua. Quis ipsum suspendisse ultrices gravida.</p>
</div>
<div class="btn" style="left:111px;top:919px;width:125px;height:42px">Learn More</div>
<div class="abs" style="left:884px;top:598px;width:281px;height:274px;background:var(--pink)"></div>
<div class="abs" style="left:660px;top:914px;width:64px;height:63px;background:var(--pink)"></div>
<div class="photo" style="left:679px;top:674px;width:409px;height:286px;background:linear-gradient(135deg,#3b3a3a,#7b7f86 55%,#2e2c2b)" role="img" aria-label="Grandmother hugging two children in winter coats"></div>

<section class="abs band-lav"></section>
<h2 style="left:0;width:1200px;text-align:center;top:1090px"><span class="dot"></span>What We Do</h2>
<div class="service" style="left:102px;top:1183px">
  <div class="ic"><svg width="60" height="60" viewBox="0 0 60 60" fill="none" stroke="#7a2e7e" stroke-width="2"><path d="M8 28L30 10l22 18"/><circle cx="30" cy="36" r="9"/><path d="M16 54c2-8 8-10 14-10s12 2 14 10"/></svg></div>
  <h3>Emergency Shelters</h3>
  <p>Lorem ipsum dolor sit ametcor adipiscing elit, sed do eiusmod tempor incididunt ut labore.</p>
</div>
<div class="service" style="left:356px;top:1183px">
  <div class="ic"><svg width="60" height="60" viewBox="0 0 60 60" fill="none" stroke="#7a2e7e" stroke-width="2"><path d="M18 28L30 16l12 12v18H18z"/><path d="M26 46V34h8v12"/><path d="M8 44c6 0 10 8 22 8s16-6 22-10"/></svg></div>
  <h3>Residential Program</h3>
  <p>Lorem ipsum dolor sit ametcor adipiscing elit, sed do eiusmod tempor incididunt ut labore.</p>
</div>
<div class="service" style="left:608px;top:1183px">
  <div class="ic"><svg width="60" height="60" viewBox="0 0 60 60" fill="none" stroke="#7a2e7e" stroke-width="2"><path d="M10 30h40c0 12-9 20-20 20S10 42 10 30z"/><circle cx="22" cy="22" r="6"/><circle cx="34" cy="20" r="7"/><path d="M40 26l6-14"/></svg></div>
  <h3>Hunger Relief</h3>
  <p>Lorem ipsum dolor sit ametcor adipiscing elit, sed do eiusmod tempor incididunt ut labore.</p>
</div>
<div class="service" style="left:862px;top:1183px">
  <div class="ic"><svg width="60" height="60" viewBox="0 0 60 60" fill="none" stroke="#7a2e7e" stroke-width="2"><path d="M30 52L10 32C2 24 8 10 18 10c6 0 10 4 12 8 2-4 6-8 12-8 10 0 16 14 8 22z"/><circle cx="30" cy="28" r="5"/><path d="M22 42c1-5 4-7 8-7s7 2 8 7"/></svg></div>
  <h3>Community Outreach</h3>
  <p>Lorem ipsum dolor sit ametcor adipiscing elit, sed do eiusmod tempor incididunt ut labore.</p>
</div>

<div class="abs" style="left:0;top:1561px;width:281px;height:273px;background:var(--pink)"></div>
<div class="abs" style="left:390px;top:1832px;width:65px;height:60px;background:var(--pink)"></div>
<div class="photo" style="left:303px;top:1635px;width:260px;height:177px;background:linear-gradient(135deg,#d9dde0,#6ea8c8 50%,#e8e5e0)" role="img" aria-label="Volunteers sorting donated clothing"></div>
<div class="photo" style="left:112px;top:1691px;width:263px;height:204px;background:linear-gradient(135deg,#c9b59c,#3f7f5b 50%,#b5813f)" role="img" aria-label="Volunteers handing out food donations"></div>
<h2 style="left:626px;top:1583px"><span class="dot"></span>Change Lives Now</h2>
<p class="abs" style="left:626px;top:1660px;width:490px">Quis ipsum suspendisse ultrices gravida. Risus commodo viverra maecenas accumsan lacus vel facilisis.</p>
<div class="amt" style="left:626px;width:88px">$50</div>
<div class="amt" style="left:728px;width:89px">$100</div>
<div class="amt" style="left:831px;width:90px">$150</div>
<div class="amt" style="left:935px;width:94px">Other</div>
<div class="btn" style="left:626px;top:1836px;width:124px;height:42px">Give Now</div>
<div class="btn outline" style="left:763px;top:1836px;width:156px;height:42px">Give Monthly</div>

<h2 style="left:0;width:1200px;text-align:center;top:1994px"><span class="dot"></span>Our Impact</h2>
<p class="abs" style="left:200px;top:2065px;width:800px;text-align:center">Lorem ipsum dolor sit amet, consectetur adipiscing elit, sed do eiusmod tempor incididunt ut labore et dolore magna aliqua. Quis ipsum suspendisse ultrices gravida. Risus commodo viverra maecenas accumsan.</p>
<div class="stat" style="left:147px;top:2157px;box-shadow:inset 0 0 18px rgba(255,94,69,.25)"><b style="color:var(--coral)">5,758</b><span>women served</span></div>
<div class="stat" style="left:394px;top:2190px;box-shadow:inset 0 0 18px rgba(74,33,131,.2)"><b style="color:var(--purple)">2,057</b><span>meals served</span></div>
<div class="stat" style="left:644px;top:2157px;box-shadow:inset 0 0 18px rgba(76,175,80,.25)"><b style="color:var(--green)">5,000</b><span>mental health<br>sessions</span></div>
<div class="stat" style="left:891px;top:2190px"><b style="color:var(--ink)">250</b><span>women housed</span></div>

<section class="abs band-beige"></section>
<div class="photo" style="left:531px;top:2407px;width:669px;height:512px;background:linear-gradient(120deg,#cdb59a 10%,#3e5a3a 50%,#c7a68a 80%);clip-path:polygon(30% 0,100% 0,100% 100%,0 100%,8% 40%)" role="img" aria-label="Mother and child eating sandwiches outdoors"></div>
<h2 style="left:111px;top:2517px"><span class="dot"></span>Real Stories</h2>
<div class="abs" style="left:111px;top:2595px;width:480px">
  <p>Lorem ipsum dolor sit amet, consectetur adipisjdcing elit, sed do eiusmod tempor incididunt ut labore et dolornke magna aliqua. Quis ipsum suspendisse ultrices gravida. Risus commodo viverra maecenas accumsan lacus vel facilisis.</p>
  <p style="margin-top:8px">Lorem ipsum dolor sit amet, consectetur adipisjdcing elit, sed do eiusmod tempor incididunt ut labore et dolornke magna aliqua. Quis ipsum suspendisse ultrices gravida.</p>
</div>
<div class="btn" style="left:111px;top:2822px;width:125px;height:42px">Learn More</div>

<h2 style="left:0;width:1200px;text-align:center;top:3006px"><span class="dot"></span>Stay Connected</h2>
<p class="abs" style="left:200px;top:3082px;width:800px;text-align:center">Lorem ipsum dolor sit amet, consectetur adipiscing elit, sed do eiusmod tempor incididunt ut labore et dolore magna aliqua. Quis ipsum suspendisse ultrices gravida. Risus commodo viverra maecenas accumsan.</p>
<div class="field" style="left:205px;width:319px">Full Name</div>
<div class="field" style="left:539px;width:319px">Email</div>
<div class="btn" style="left:870px;top:3173px;width:125px;height:42px">Sign Up</div>

<footer class="abs footer">
  <div class="brand"><i></i>Lumina</div>
  <div class="social"><i></i><i></i><i></i></div>
  <div class="fcol" style="left:400px">
    <h4>CONTACT US</h4>
    <div class="fline"><svg width="12" height="16" viewBox="0 0 12 16"><path d="M6 0a6 6 0 0 0-6 6c0 4.5 6 10 6 10s6-5.5 6-10a6 6 0 0 0-6-6zm0 8.5A2.5 2.5 0 1 1 6 3.5a2.5 2.5 0 0 1 0 5z" fill="#fff"/></svg><span style="line-height:26px;margin-top:-5px">Lumina women's shelter,<br>Address comes here.</span></div>
    <div class="fline" style="margin-top:14px"><svg width="14" height="14" viewBox="0 0 14 14"><path d="M3 0l3 3-2 2c1 2 3 4 5 5l2-2 3 3-2 3C6 14 0 8 0 3z" fill="#fff"/></svg><span style="margin-top:-4px">+1-555-014-2290</span></div>
    <div class="fline" style="margin-top:16px"><svg width="15" height="12" viewBox="0 0 15 12"><rect width="15" height="12" fill="#fff"/><path d="M0 0l7.5 6L15 0" stroke="#8d3c7a" stroke-width="1.5" fill="none"/></svg><span style="margin-top:-4px">hello@luminashelter.org</span></div>
  </div>
  <div class="fcol" style="left:769px"><h4>QUICK LINKS</h4><ul><li>Campaign</li><li>About</li><li>What We Do</li><li>Real Stories</li><li>Ways To Give</li></ul></div>
  <div class="fcol" style="left:947px"><h4>OTHER LINKS</h4><ul><li>Get Involved</li><li>Contact</li><li>Terms &amp; Conditions</li><li>Privacy Policy</li></ul></div>
  <div class="copy">2023 Lumina Women's Shelter. All Rights Reserved.</div>
</footer>

</body>
</html>
```